Business card design needed

New company based in Brisbane, Australia. Brindle Systems. The business is focused on the delivery of network architecture design and deployment. We will provide both services and the sale of the necessary equipment to deliver the service. Cloud computing is an important element of our focus as this is an emerging market for enterprises in Queensland. Our target marketplace is medium to large corporations with complex infrastructure requirements. IT Management and above will be the typical entry point for us into these accounts. We would like to see the use of various shade of green, design should be clutter free and impress stability, trust and growth.
Updates
Hey Everyone
Just we let you all know we have changed this project to 'committed' payment status.
Looking forward to seeing the designs! Thanks for your efforts.
Best Regards
Marcus
Industry/Entity Type
Architecture
Contact Information for Business Card
Brindle Systems, Marcus Doyle, Sales Director, Level 14 Harlow Tower, 58 Penfold Street, Brisbane QLD 4000, Ph +61 7 3904 2267, M +61 4 4926 1573, E marcus.doyle@brindlesystems-example.com.au
Look and feel
Each slider illustrates characteristics of the customer's brand and the style your logo design should communicate.

```html
<!DOCTYPE html>
<html lang="en">
<head>
<meta charset="utf-8">
<title>Brindle Systems – Business Card</title>
<link rel="stylesheet" href="https://fonts.googleapis.com/css2?family=Arimo:wght@400&display=swap">
<style>
  :root {
    --card-bg: #e6ebe8;
    --green-deep: #1e8a1a;
    --green-mid: #22a51a;
    --green-bright: #55e01f;
    --green-brand: #2dbd14;
  }
  html, body {
    margin: 0;
    padding: 0;
    width: 1200px;
    height: 741px;
    overflow: hidden;
    background: var(--card-bg);
  }
  .card {
    position: relative;
    width: 1200px;
    height: 741px;
    background: var(--card-bg);
    font-family: "Arimo", Arial, sans-serif;
    font-weight: 400;
    line-height: 1;
  }
  .card p { margin: 0; position: absolute; white-space: nowrap; }

  .brand {
    position: absolute;
    top: 50px;
    right: 42px;
    display: flex;
    align-items: center;
    gap: 18px;
  }
  .brand-dot { width: 70px; height: 70px; display: block; }
  .brand-name {
    font-size: 58px;
    color: var(--green-brand);
    white-space: nowrap;
  }

  .person-name { left: 43px; top: 231px; font-size: 65px; color: var(--green-deep); }
  .person-role { left: 43px; top: 304px; font-size: 52px; color: var(--green-bright); }

  .contact { left: 41px; color: var(--green-mid); }
  .contact-phone  { top: 429px; font-size: 52px; }
  .contact-mobile { top: 502px; font-size: 52px; }
  .contact-email  { top: 582px; font-size: 40px; }

  .address {
    left: 0;
    width: 1200px;
    text-align: center;
    top: 679px;
    font-size: 28px;
    color: var(--green-mid);
  }
</style>
</head>
<body>
  <div class="card">
    <div class="brand">
      <svg class="brand-dot" viewBox="0 0 70 70" aria-hidden="true">
        <circle cx="35" cy="35" r="35" fill="var(--green-brand)"/>
      </svg>
      <span class="brand-name">Brindle Systems</span>
    </div>

    <p class="person-name">Marcus Doyle</p>
    <p class="person-role">Sales Director</p>

    <p class="contact contact-phone">P: +61 7 3904 2267</p>
    <p class="contact contact-mobile">M: +61 4 4926 1573</p>
    <p class="contact contact-email">E: marcus.doyle@brindlesystems-example.com.au</p>

    <p class="address">Level 14 Harlow Tower, 58 Penfold Street, Brisbane QLD 4000</p>
  </div>
</body>
</html>
```